Visit card

Industry/Entity Type

Health Care

Contact Information for Business Card

O VITALE SYSTEMES
Odile Ferrandi - chef de Projet

Requirements
Must have
• 318 Hector Delaunay Street 58210 BÉTHUNE Tel: 33 (0) 387 419 264 Mobile: 06 42 93 17 58 Web: www.vobelasystems.example Contact: o.ferrandi@o-vitalesystemes.example
Should not have
• Respect for color

```html
<!DOCTYPE html>
<html lang="fr">
<head>
<meta charset="utf-8">
<title>O VITALE SYSTEMES – Business Card</title>
<link rel="stylesheet" href="https://fonts.googleapis.com/css2?family=Arimo:wght@400;700&display=swap">
<style>
  :root {
    --page-bg: #2b2b2e;
    --card-dark: #4a4a4d;
    --card-dark-deco: #3f3f42;
    --card-light: #ffffff;
    --ink: #3c3c3e;
    --ink-soft: #555558;
    --brand-red: #e5232b;
    --deco-light: #efefef;
  }
  * { box-sizing: border-box; margin: 0; padding: 0; }
  html, body { width: 1200px; height: 800px; overflow: hidden; }
  body {
    background: var(--page-bg);
    font-family: "Arimo", Arial, sans-serif;
    position: relative;
  }
  .card {
    position: absolute;
    top: 245px;
    width: 540px;
    height: 310px;
    border-radius: 22px;
    overflow: hidden;
  }
  .card--front { left: 40px; background: var(--card-dark); }
  .card--back { left: 620px; background: var(--card-light); }

  .deco-ring {
    position: absolute;
    border-radius: 50%;
  }
  .card--front .deco-ring {
    width: 300px; height: 300px; left: 40px; top: 5px;
    border: 38px solid var(--card-dark-deco);
  }
  .card--back .deco-ring {
    width: 260px; height: 260px; right: 30px; top: -40px;
    border: 34px solid var(--deco-light);
  }

  .brand { position: absolute; display: flex; align-items: center; gap: 14px; }
  .brand__dot {
    width: 58px; height: 58px; border-radius: 50%;
    background: var(--brand-red);
    flex: none;
  }
  .brand__name {
    font-weight: 700; font-size: 27px; letter-spacing: 1px; line-height: 1.05;
  }
  .card--front .brand { left: 150px; top: 122px; }
  .card--front .brand__name { color: #ffffff; }
  .card--back .brand { left: 36px; top: 48px; }
  .card--back .brand__dot { width: 50px; height: 50px; }
  .card--back .brand__name { color: var(--ink); font-size: 23px; }

  .person { position: absolute; left: 36px; top: 150px; }
  .person__name { font-weight: 700; font-size: 17px; color: var(--ink); text-transform: uppercase; }
  .person__role { font-size: 14px; color: var(--brand-red); margin-top: 2px; }
  .divider {
    position: absolute; left: 36px; right: 36px; top: 196px;
    height: 1px; background: var(--brand-red);
  }
  .contact { position: absolute; left: 36px; top: 206px; list-style: none; }
  .contact li {
    display: flex; align-items: center; gap: 8px;
    font-size: 12px; color: var(--ink-soft); margin-bottom: 4px;
  }
  .contact svg { width: 14px; height: 14px; flex: none; }
  .address {
    position: absolute; right: 36px; top: 206px; text-align: right;
    font-style: normal;
    font-size: 12.5px; line-height: 1.4; color: var(--ink-soft);
  }
  .footer-band {
    position: absolute; left: 0; right: 0; bottom: 0; height: 22px;
    background: var(--ink);
  }
  .web-band {
    position: absolute; right: 0; bottom: 0; height: 32px; width: 250px;
    background: var(--brand-red); color: #fff;
    font-size: 12.5px; display: flex; align-items: center; justify-content: center;
  }
</style>
</head>
<body>
  <section class="card card--front" aria-label="Card front">
    <div class="deco-ring"></div>
    <div class="brand">
      <span class="brand__dot"></span>
      <span class="brand__name">O VITALE<br>SYSTEMES</span>
    </div>
  </section>

  <section class="card card--back" aria-label="Card back">
    <div class="deco-ring"></div>
    <div class="brand">
      <span class="brand__dot"></span>
      <span class="brand__name">O VITALE<br>SYSTEMES</span>
    </div>
    <div class="person">
      <p class="person__name">Odile Ferrandi</p>
      <p class="person__role">Manager</p>
    </div>
    <div class="divider"></div>
    <address class="address">318 Hector<br>Delaunay Street<br>58210 BÉTHUNE</address>
    <ul class="contact">
      <li>
        <svg viewBox="0 0 14 14"><circle cx="7" cy="7" r="6.2" fill="none" stroke="#e5232b" stroke-width="1.2"/><path d="M5 4l1 1.6-.7.8c.4.9 1 1.5 1.9 1.9l.8-.7L9.6 8.6 9 9.8C6.8 9.6 4.4 7.2 4.2 5z" fill="#e5232b"/></svg>
        33 (0) 387 419 264
      </li>
      <li>
        <svg viewBox="0 0 14 14"><circle cx="7" cy="7" r="6.2" fill="none" stroke="#e5232b" stroke-width="1.2"/><rect x="5" y="3.6" width="4" height="6.8" rx="0.7" fill="none" stroke="#e5232b" stroke-width="1"/></svg>
        06 42 93 17 58
      </li>
      <li>
        <svg viewBox="0 0 14 14"><circle cx="7" cy="7" r="6.2" fill="none" stroke="#e5232b" stroke-width="1.2"/><rect x="4" y="4.8" width="6" height="4.4" fill="none" stroke="#e5232b" stroke-width="1"/><path d="M4 4.8l3 2.4 3-2.4" fill="none" stroke="#e5232b" stroke-width="1"/></svg>
        o.ferrandi@o-vitalesystemes.example
      </li>
    </ul>
    <div class="footer-band"></div>
    <div class="web-band">www.vobelasystems.example</div>
  </section>
</body>
</html>
```